Martial Arts Website

Redevelopment of existing martial arts website.

The academy teaches traditional shaolin martial arts, including Shaolin Kung Fu, Wu Shu, Tai Chi, Qigong and Wing Chun and the site needs to reflect the traditional roots (eg, no tacky boxing imagery)

Existing website is www.copperheron.com.au to get a feel for the desired color scheme (black, green and red). The exact colors can be tweaked though. Please only reuse the logo and font (Karate) - there isnt anything else from the current design that needs to remain.

The current website includes links to a YouTube channel that includes demonstrations of the training conducted to better guide the design.

The new website site map will be:
1. Home
2. Programs - summary page describing each form of training
a. Tiny Otters
b. Kids Kung Fu
c. Youth Kung Fu
d. Adults Kung Fu
e. Wing Chun
f. Tai Chi & Qigong
g. Weaponry Classes
h. 72 Arts of Shaolin Conditioning Program
i. Acrobatics and Wu Shu
j. Fitness Boxing
3. Timetable
4. Coaches - summary page describing all coaches
a. Sifu (Master)
b. Sihing Lou
c. Sihing Kim
d. Sihing Felix
X. ... up to 10 or so coaches
5. Member Zone
6. Contact Us
Updates

Logo now attached to brief - sorry I only have it in PDF

Just to clarify, I am only expecting a PSD design - no HTML required

Reason: Thanks for the designs, we love a lot of them just require a little extra time to tweak the designs and establish the potential. Thanks for your understanding and efforts.

Target Market(s)

Parents, teenagers, young adults, adults, elderly

Industry/Entity Type

Training

Requirements
Must have
• Chinese kung fu dragon imagery throughout the background
Links to Facebook and YouTube channel
Promo/icon in the header "Try 2 free classes now"
Home page should include an embedded YouTube video

```html
<!DOCTYPE html>
<html lang="en">
<head>
<meta charset="utf-8">
<title>Copper Heron Martial Arts Academy</title>
<link rel="stylesheet" href="https://fonts.googleapis.com/css2?family=Cinzel:wght@700&family=Questrial&family=Nunito:ital,wght@1,900&family=Arimo:wght@400;700&display=swap">
<style>
  :root {
    --ink: #111;
    --green: #2e8b2a;
    --green-deep: #1f6b1e;
    --title-green: #3fae2a;
    --red: #c23a1c;
    --panel: rgba(255,255,255,0.78);
    --card: rgba(255,255,255,0.93);
    --white: #fff;
  }
  * { margin: 0; padding: 0; box-sizing: border-box; }
  html, body { width: 1200px; height: 900px; overflow: hidden; background: #000; }
  body { position: relative; font-family: "Arimo", Arial, sans-serif; color: var(--ink); }

  .backdrop {
    position: absolute; inset: 0;
    background:
      radial-gradient(ellipse at 50% 10%, rgba(0,0,0,0.9) 0%, rgba(0,0,0,0.6) 40%, transparent 70%),
      radial-gradient(ellipse at 10% 70%, #7a4a3c 0%, transparent 45%),
      radial-gradient(ellipse at 92% 60%, #8a5242 0%, transparent 45%),
      linear-gradient(180deg, #151212 0%, #3e2c27 45%, #6a5048 75%, #b9aea6 92%, #2a2220 100%);
  }

  .brand-mark {
    position: absolute; left: 140px; top: 25px; width: 130px; height: 130px;
    border-radius: 50%; background: #0c0c0c; border: 5px solid var(--title-green);
  }
  .brand-name {
    position: absolute; left: 288px; top: 64px;
    font-family: "Cinzel", serif; font-weight: 700; font-size: 23px;
    color: var(--title-green); letter-spacing: 0.5px;
  }
  .brand-tagline {
    position: absolute; left: 291px; top: 96px;
    font-family: "Cinzel", serif; font-weight: 700; font-size: 16px;
    color: var(--white); letter-spacing: 1px;
  }

  .promo { position: absolute; left: 893px; top: 3px; width: 170px; height: 170px; }
  .promo-text {
    position: absolute; left: 0; top: 36px; width: 170px; transform: rotate(-8deg);
    text-align: center; font-family: "Nunito", sans-serif; font-style: italic; font-weight: 900;
    font-size: 22px; line-height: 23px; color: var(--white);
  }

  .panel { position: absolute; left: 122px; top: 175px; width: 952px; height: 600px; background: var(--panel); }

  .main-nav { position: absolute; left: 23px; top: 0; height: 61px; width: 900px; }
  .main-nav a {
    position: absolute; top: 0; height: 61px; line-height: 61px;
    font-family: "Questrial", sans-serif; font-size: 15.5px; letter-spacing: 1.6px;
    color: var(--ink); text-decoration: none; transform: translateX(-50%); white-space: nowrap;
  }
  .main-nav a.is-active { background: var(--green); color: var(--white); width: 89px; text-align: center; transform: none; left: 0; }

  .video {
    position: absolute; left: 55px; top: 104px; width: 509px; height: 281px;
    background: radial-gradient(ellipse at 65% 15%, #9a9a9a 0%, #3a3a3a 35%, #111 75%);
  }
  .video svg { position: absolute; left: 220px; top: 110px; }

  .welcome-title { position: absolute; left: 55px; top: 412px; font-size: 16px; font-weight: 700; color: var(--red); }
  .welcome-body { position: absolute; left: 55px; top: 450px; width: 520px; font-size: 12px; line-height: 14px; color: #222; }

  .card { position: absolute; left: 618px; width: 281px; background: var(--card); }
  .card-title { font-size: 14px; font-weight: 700; color: var(--red); letter-spacing: 0.3px; }
  .news { top: 103px; height: 197px; padding: 19px 19px; }
  .news p { font-size: 12px; line-height: 15px; margin-top: 15px; }
  .news .more { position: absolute; right: 15px; bottom: 13px; margin: 0; }
  .newsletter { top: 311px; height: 56px; padding: 21px 19px; }
  .newsletter svg { position: absolute; right: 23px; top: 13px; }
  .accreditation { top: 377px; height: 163px; padding: 19px 21px; }
  .badges { display: flex; gap: 25px; margin-top: 26px; align-items: center; }

  .social { position: absolute; left: 839px; top: 553px; display: flex; gap: 7px; }
  .social span { width: 26px; height: 26px; border-radius: 3px; }

  .copyright {
    position: absolute; top: 827px; left: 0; width: 1190px; text-align: center;
    font-size: 14px; font-weight: 700; color: #000;
  }
</style>
</head>
<body>
  <div class="backdrop" role="img" aria-label="Sepia photograph of shaolin monks performing kung fu on stage"></div>

  <header>
    <div class="brand-mark"></div>
    <div class="brand-name">Copper Heron Martial Arts Academy</div>
    <div class="brand-tagline">Traditional Kung Fu and Tai Chi Training Centre</div>

    <div class="promo">
      <svg width="170" height="170" viewBox="0 0 170 170">
        <polygon fill="#fff" points="85,0 94,22 110,4 113,27 133,14 129,37 152,30 142,51 165,50 150,67 170,75 152,87 168,102 146,105 156,126 134,123 138,147 117,138 113,162 98,148 85,170 72,148 57,162 53,138 32,147 36,123 14,126 24,105 2,102 18,87 0,75 20,67 5,50 28,51 18,30 41,37 37,14 57,27 60,4 76,22"/>
        <circle cx="85" cy="86" r="63" fill="#111"/>
        <circle cx="85" cy="86" r="58" fill="var(--green-deep)"/>
      </svg>
      <div class="promo-text">Try<br>2 free<br>classes<br>now</div>
    </div>
  </header>

  <main class="panel">
    <nav class="main-nav">
      <a class="is-active" href="#">HOME</a>
      <a href="#" style="left:196px">PROGRAMS</a>
      <a href="#" style="left:361px">TIMETABLE</a>
      <a href="#" style="left:518px">COACHES</a>
      <a href="#" style="left:681px">MEMBER ZONE</a>
      <a href="#" style="left:855px">CONTACT US</a>
    </nav>

    <div class="video" role="img" aria-label="Video still: silhouette of a martial artist kicking against the sky">
      <svg width="60" height="60" viewBox="0 0 60 60">
        <circle cx="30" cy="30" r="27" fill="none" stroke="#fff" stroke-width="3.5"/>
        <polygon points="22,16 22,44 45,30" fill="#fff"/>
      </svg>
    </div>

    <h1 class="welcome-title">Welcome to Copper Heron Martial Arts Academy - NSW Australia</h1>
    <p class="welcome-body">
      Traditional Shaolin Kung Fu, Wing Chun Kung Fu, Tai Chi &amp; Qigong for all ages and physical capabilities.<br>
      Our training centre location is:<br>
      Unit 7, 22 Harlow Street, Brookvale West, NSW, 2790
    </p>

    <section class="card news">
      <h2 class="card-title">NEWS &amp; UPDATES</h2>
      <p>Kids Kung Fu Holiday Workshop 18thApril 2012</p>
      <p>Kwoon Open Day 12th All welcome.</p>
      <p>Copper Heron Hosts: "A day with the masters".</p>
      <p class="more">more..</p>
    </section>

    <section class="card newsletter">
      <h2 class="card-title">DOWNLOAD NEWSLETTER</h2>
      <svg width="30" height="30" viewBox="0 0 30 30">
        <circle cx="15" cy="15" r="14" fill="#e8e8e8" stroke="#bbb"/>
        <rect x="12" y="7" width="6" height="8" fill="#8b1414"/>
        <polygon points="8,14 22,14 15,22" fill="#8b1414"/>
      </svg>
    </section>

    <section class="card accreditation">
      <h2 class="card-title">ACCREDITATION</h2>
      <div class="badges">
        <svg width="62" height="62"><circle cx="31" cy="31" r="30" fill="#c47a2a"/></svg>
        <svg width="62" height="36"><rect x="0" y="0" width="62" height="36" rx="16" fill="#222"/></svg>
        <svg width="54" height="42"><rect x="0" y="0" width="54" height="42" rx="4" fill="#2a55a0"/></svg>
      </div>
    </section>

    <div class="social">
      <span style="background:#3b5998"></span>
      <span style="background:#c4302b"></span>
    </div>
  </main>

  <footer class="copyright">Copyright © 2012 - Copper Heron Martial Arts Pty Ltd. Brookvale West NSW 2790</footer>
</body>
</html>
```